Redesign of the labels for our cosmetic brand Su Dulcaria

We need to redesign all the labels for our pharmaceutical cosmetic brand. It must be inspired in the old time apothecary and compounding pharmacies. Our aim is to emulate old pharmacy bottles and jars, as our cosmetics are formulated as they used to be prepared; with the highest amount of actives and always based in Nature
We have attached our actual catalogue so you can get an idea of who we are. Also we have attached some of our old style labels. We changed them last year but they havent been atractive enough

Target Market(s)

Pharmaceutical cosmetics

Industry/Entity Type

Pharmaceutical

Requirements
Must have
• The labels must have a vintage touch, like old pharmacy jars

```html
<!DOCTYPE html>
<html lang="es">
<head>
<meta charset="utf-8">
<title>Su Dulcaria – etiquetas</title>
<link rel="stylesheet" href="https://fonts.googleapis.com/css2?family=Quicksand:wght@500&display=swap">
<style>
  :root {
    --backdrop-top: #eef2f6;
    --backdrop-bottom: #d6dde5;
    --label-light: #fbf6ea;
    --label-deep: #eddfc0;
    --label-rim: #7a5a34;
    --label-inner-line: #c9ad7c;
    --ink: #6a4c2b;
  }
  html, body {
    margin: 0;
    padding: 0;
    overflow: hidden;
  }
  body {
    width: 741px;
    height: 1200px;
    background: linear-gradient(180deg, var(--backdrop-top), var(--backdrop-bottom));
    position: relative;
    font-family: "Quicksand", sans-serif;
  }
  .label {
    position: absolute;
  }
  .label svg {
    position: absolute;
    inset: 0;
    width: 100%;
    height: 100%;
    overflow: visible;
  }
  .label__content {
    position: absolute;
    left: 0;
    right: 0;
    text-align: center;
  }
  .brand-name {
    color: var(--ink);
    font-weight: 500;
    letter-spacing: 0.5px;
    margin: 0;
    line-height: 1;
  }
  .divider {
    display: block;
    margin: 0 auto;
  }
  .label--arched { left: 69px; top: 600px; width: 228px; height: 340px; }
  .label--arched .label__content { top: 168px; }
  .label--arched .brand-name { font-size: 36px; }

  .label--crest { left: 341px; top: 392px; width: 380px; height: 208px; }
  .label--crest .label__content { top: 92px; }
  .label--crest .brand-name { font-size: 36px; }

  .label--tablet { left: 363px; top: 772px; width: 320px; height: 204px; }
  .label--tablet .label__content { top: 78px; }
  .label--tablet .brand-name { font-size: 34px; }
</style>
</head>
<body>
  <svg width="0" height="0" aria-hidden="true" style="position:absolute">
    <defs>
      <linearGradient id="paper" x1="0" y1="0" x2="0" y2="1">
        <stop offset="0" stop-color="#fbf6ea"/>
        <stop offset="1" stop-color="#eddfc0"/>
      </linearGradient>
    </defs>
  </svg>

  <section class="label label--arched" aria-label="Etiqueta de botella">
    <svg viewBox="0 0 228 340" preserveAspectRatio="none">
      <path d="M4 336 V92 Q4 4 114 4 Q224 4 224 92 V336 Z" fill="url(#paper)" stroke="var(--label-rim)" stroke-width="4"/>
      <path d="M13 327 V94 Q13 13 114 13 Q215 13 215 94 V327 Z" fill="none" stroke="var(--label-inner-line)" stroke-width="1.5"/>
    </svg>
    <div class="label__content">
      <p class="brand-name">su dulcaria</p>
      <svg class="divider" width="150" height="16" viewBox="0 0 150 16" style="position:static">
        <line x1="6" y1="8" x2="144" y2="8" stroke="var(--ink)" stroke-width="1.2"/>
        <circle cx="75" cy="8" r="3" fill="var(--ink)"/>
      </svg>
    </div>
  </section>

  <section class="label label--crest" aria-label="Etiqueta de tarro">
    <svg viewBox="0 0 380 208" preserveAspectRatio="none">
      <path d="M4 60 Q4 36 30 34 Q90 30 110 16 Q124 4 150 4 H230 Q256 4 270 16 Q290 30 350 34 Q376 36 376 60 V168 Q376 204 340 204 H40 Q4 204 4 168 Z" fill="url(#paper)" stroke="var(--label-rim)" stroke-width="4"/>
      <path d="M13 62 Q13 45 32 43 Q94 38 116 23 Q128 13 150 13 H230 Q252 13 264 23 Q286 38 348 43 Q367 45 367 62 V166 Q367 195 338 195 H42 Q13 195 13 166 Z" fill="none" stroke="var(--label-inner-line)" stroke-width="1.5"/>
    </svg>
    <div class="label__content">
      <p class="brand-name">su dulcaria</p>
      <svg class="divider" width="210" height="20" viewBox="0 0 210 20" style="position:static">
        <line x1="6" y1="10" x2="204" y2="10" stroke="var(--ink)" stroke-width="1.2"/>
        <circle cx="105" cy="10" r="3" fill="var(--ink)"/>
      </svg>
    </div>
  </section>

  <section class="label label--tablet" aria-label="Etiqueta de frasco">
    <svg viewBox="0 0 320 204" preserveAspectRatio="none">
      <rect x="4" y="4" width="312" height="196" rx="18" fill="url(#paper)" stroke="var(--label-rim)" stroke-width="4"/>
      <rect x="13" y="13" width="294" height="178" rx="12" fill="none" stroke="var(--label-inner-line)" stroke-width="1.5"/>
    </svg>
    <div class="label__content">
      <p class="brand-name">su dulcaria</p>
      <svg class="divider" width="220" height="20" viewBox="0 0 220 20" style="position:static">
        <line x1="6" y1="10" x2="214" y2="10" stroke="var(--ink)" stroke-width="1.2"/>
        <circle cx="110" cy="10" r="3" fill="var(--ink)"/>
      </svg>
    </div>
  </section>
</body>
</html>
```